Wordpress Design Project - Development Company

We need a website for our Developments company "KT Developments". I would like to use Wordpress for its simplicity to update and added features.
We develop/build and sell Townhouses/Houses and Land around Brisbane, Qld. Initially we require a Web presence with no advanced features. We will develop the user logins and other features at a future point in time. We are undecided on having a single page with most of the detail or to have more detail on linked pages, we will review the options put forward. We have added a Sitemap and possible Frontpage sketch
Some sites for examples we have thought work similar and well:
http://www.ferncastle.com.au/index.htm
http://tallwillowplains.com.au/
http://www.mqholloway.com.au
http://coralframe.com.au/
http://www.pelham.com.au/queensland.aspx
http://www.meridale.com.au/
I've attached our newly created Business Cards and we are also working on a logo for the company within the next couple of days which may or may not be the same as the Business Card
Any questions please ask
Updates
Please update the main picture on your webpages to the attached so we can compare equally http://files.filevaultex.com/u/50927361/Img1c.jpg
Target Market(s)
Townhouse/House/Land buyers & Salespeople
Industry/Entity Type
Business
Look and feel
Each slider illustrates characteristics of the customer's brand and the style your logo design should communicate.

```html
<!DOCTYPE html>
<html lang="en">
<head>
<meta charset="utf-8">
<title>KT Developments P/L</title>
<link rel="stylesheet" href="https://fonts.googleapis.com/css2?family=Noto+Sans:wght@400;700&family=Oswald:wght@300;400&family=Josefin+Sans:wght@300&display=swap">
<style>
:root{
  --red:#c8101e;
  --ink:#222;
  --text:#555;
  --muted:#9a9a9a;
  --soft:#cfcac4;
  --page:#ffffff;
  --backdrop:#ececec;
  --box:#f2f2f2;
  --line:#d8d8d8;
  --grey-head:#a9a9a9;
}
*{box-sizing:border-box;margin:0;padding:0}
html,body{width:1171px;height:1200px;overflow:hidden}
body{background:var(--backdrop);font-family:"Noto Sans",sans-serif;color:var(--text);position:relative}
a{color:inherit;text-decoration:none}
.page{position:absolute;left:88px;top:0;width:996px;height:1110px;background:var(--page);box-shadow:0 0 6px rgba(0,0,0,.15)}
.abs{position:absolute}

.brand{left:114px;top:38px;display:flex;align-items:center;gap:14px}
.brand-mark{width:40px;height:40px;background:var(--red)}
.brand-name{font-size:26px;letter-spacing:4px;color:var(--ink);font-weight:400}

.util-links{right:108px;top:17px;font-size:12px;font-weight:700;color:#444;display:flex;gap:18px}
.util-links span.sep{color:#999;font-weight:400}
.contact-top{right:108px;font-size:13px;color:#666;display:flex;align-items:center;gap:6px}
.contact-top b{color:var(--red);font-size:14px}
.contact-top.phone{top:53px}
.contact-top.email{top:76px}

.main-nav{left:108px;top:121px;width:956px;height:51px;border-radius:6px;
  background:linear-gradient(#fafafa,#dcdcd8);border:1px solid #c9c9c4;
  box-shadow:0 2px 2px rgba(0,0,0,.12);display:grid;
  grid-template-columns:142px 169px 188px 161px 146px 1fr}
.main-nav a{display:flex;align-items:center;justify-content:center;font-size:14px;font-weight:700;color:#555;border-right:1px solid #c4c4be}
.main-nav a:last-child{border-right:0}

.hero{left:108px;top:193px;width:956px;height:354px;border-radius:5px;overflow:hidden;
  background:linear-gradient(180deg,#8fb8dd 0%,#cfe0ec 30%,#c9c3b6 55%,#8b8a86 80%,#6f6f6d 100%)}
.hero-title{position:absolute;top:30px;width:100%;text-align:center;font-family:"Josefin Sans",sans-serif;font-weight:300;font-size:52px;color:#fff;letter-spacing:1px}
.hero-arrow{position:absolute;top:103px;width:62px;height:149px;background:rgba(240,240,240,.55)}
.hero-arrow.prev{left:0;border-radius:0 6px 6px 0}
.hero-arrow.next{right:0;border-radius:6px 0 0 6px}
.hero-arrow svg{position:absolute;top:38px;left:12px}
.hero-caption{position:absolute;left:0;bottom:0;width:100%;height:73px;background:rgba(40,40,40,.55);
  color:#fff;font-size:14px;text-transform:uppercase;padding:15px 20px;line-height:23px}

.side-box{left:108px;width:242px;border-radius:6px;background:var(--box);overflow:hidden}
.side-box h2{font-family:"Oswald",sans-serif;font-weight:400;font-size:20px;color:#fff;padding:0 15px;height:42px;line-height:42px}
.news-box{top:578px;height:292px;border:1px solid var(--red)}
.news-box h2{background:var(--red)}
.news-list{list-style:none;padding:10px 14px 0 14px}
.news-list li{font-size:13px;line-height:19px;padding:5px 0 8px 14px;border-bottom:1px dotted #ccc;position:relative}
.news-list li:last-child{border-bottom:0}
.news-list li::before{content:"›";position:absolute;left:0;top:4px;color:#777}
.read-more{display:block;text-align:right;font-size:13px;font-weight:700;color:#555;padding:0 14px}
.contact-box{top:902px;height:186px;border:1px solid #cfcfcf}
.contact-box h2{background:var(--grey-head)}
.contact-box address{font-style:normal;font-size:13px;line-height:20.5px;color:#666;padding:12px 20px}

.welcome{left:382px;top:570px;width:674px}
.welcome h1{font-family:"Oswald",sans-serif;font-weight:300;font-size:29px;color:var(--soft);margin-bottom:8px}
.welcome h1 span{color:var(--red);font-weight:400}
.welcome p{font-size:13px;line-height:18.5px;color:var(--muted);margin-bottom:18px}
.rule{left:382px;top:818px;width:694px;height:4px;background:var(--red)}

.project{top:857px;width:215px}
.project h3{font-size:13px;font-weight:700;color:#444;text-transform:uppercase;margin-bottom:16px}
.project-photo{width:208px;height:107px;border:3px solid #ddd}
.project ul{list-style:none;margin-top:22px}
.project li{font-size:12px;color:#444;line-height:26.5px;padding-left:12px;position:relative;white-space:nowrap}
.project li::before{content:"›";position:absolute;left:0;color:#555}

.footer-links{left:97px;top:1133px;font-size:12px;color:#777;display:flex;gap:10px}
.footer-call{left:97px;top:1155px;font-family:"Oswald",sans-serif;font-size:23px;color:var(--soft)}
.footer-call b{color:var(--red);font-weight:400}
.copyright{right:96px;top:1133px;font-size:12px;color:#777}
.social{right:96px;top:1161px;display:flex;gap:6px}
.social span{width:16px;height:16px;border-radius:2px}
</style>
</head>
<body>
<div class="page"></div>

<div class="abs brand"><span class="brand-mark"></span><span class="brand-name">KT Developments P/L</span></div>

<nav class="abs util-links"><a href="#">Home</a><span class="sep">|</span><a href="#">Sitemap</a><span class="sep">|</span><a href="#">Disclaimer/Privacy Policy</a></nav>
<div class="abs contact-top phone">
  <svg width="15" height="13" viewBox="0 0 15 13" aria-hidden="true"><path d="M2 1h3l1 3-2 1a7 7 0 0 0 4 4l1-2 3 1v3c0 1-1 1-2 1A11 11 0 0 1 1 3c0-1 0-2 1-2z" fill="#c8101e"/></svg>
  Phone: <b>3812 4471</b></div>
<div class="abs contact-top email">
  <svg width="15" height="10" viewBox="0 0 15 10" aria-hidden="true"><rect width="15" height="10" fill="#c8101e"/><path d="M0 0l7.5 6L15 0" stroke="#fff" fill="none"/></svg>
  Email: <b>hello@ktdev.example</b></div>

<nav class="abs main-nav">
  <a href="#">Overview</a><a href="#">Current Projects</a><a href="#">Completed Projects</a><a href="#">Future Projects</a><a href="#">Latest News</a><a href="#">Contact Us</a>
</nav>

<section class="abs hero" role="img" aria-label="Photo of modern two-storey townhouses on a sunny street with residents walking by">
  <div class="hero-title">A NEW LIGHT ON LIVING</div>
  <a class="hero-arrow prev" href="#" aria-label="Previous"><svg width="38" height="72" viewBox="0 0 38 72"><path d="M34 2L4 36l30 34" stroke="#c8101e" stroke-width="4" fill="none"/></svg></a>
  <a class="hero-arrow next" href="#" aria-label="Next"><svg width="38" height="72" viewBox="0 0 38 72"><path d="M4 2l30 34L4 70" stroke="#c8101e" stroke-width="4" fill="none"/></svg></a>
  <p class="hero-caption">Lorem Ipsum is simply dummy text of the printing and typesetting industry. Lorem Ipsum has been the industry's standard dummy text ever since the 1500s...</p>
</section>

<aside class="abs side-box news-box">
  <h2>LATEST NEWS</h2>
  <ul class="news-list">
    <li>Morbi fringilla quam sit amet dui tempus facilisis.</li>
    <li>Morbi facilisis augue non mauris dapibus tristique.</li>
    <li>Morbi fringilla quam sit amet dui tempus facilisis.</li>
    <li>Morbi facilisis augue non mauris dapibus tristique.</li>
  </ul>
  <a class="read-more" href="#">Read more...</a>
</aside>

<aside class="abs side-box contact-box">
  <h2>CONTACT US NOW!</h2>
  <address>Phone: 3812 4471<br>Mobile: 0400 555 218<br>Email: hello@ktdev.example<br><br>PO Box 5512<br>Elmwood Vale QLD 4200</address>
</aside>

<section class="abs welcome">
  <h1>WELCOME TO <span>KT DEVELOPMENTS P/L</span></h1>
  <p>Lorem Ipsum is simply dummy text of the printing and typesetting industry. Lorem Ipsum has been the industry's standard dummy text ever since the 1500s, when an unknown printer took a galley of type and scrambled it to make a type specimen book.</p>
  <p>It has survived not only five centuries, but also the leap into electronic typesetting, remaining essentially unchanged.</p>
  <p>It was popularised in the 1960s with the release of Letraset sheets containing Lorem Ipsum passages, and more recently with desktop publishing software like Aldus PageMaker including versions of Lorem Ipsum.</p>
</section>
<div class="abs rule"></div>

<section class="abs project" style="left:382px">
  <h3>Current Projects</h3>
  <div class="project-photo" role="img" aria-label="Photo of a family enjoying a picnic outdoors" style="background:linear-gradient(135deg,#e9e3d6,#b9c9a0 60%,#7da05a)"></div>
  <ul><li>Fusce id magna metus, ut interdum</li><li>Duis in eros in ipsum porttitor mattis</li><li>Etiam ac urna id velit eleifend ultric</li></ul>
</section>
<section class="abs project" style="left:615px">
  <h3>Complrira Projects</h3>
  <div class="project-photo" role="img" aria-label="Photo of a completed home with landscaped garden path" style="background:linear-gradient(180deg,#9fc3df,#c9a88c 50%,#6e8a55)"></div>
  <ul><li>Fusce id magna metus, ut interdum</li><li>Duis in eros in ipsum porttitor mattis</li><li>Etiam ac urna id velit eleifend ultric</li></ul>
</section>
<section class="abs project" style="left:850px">
  <h3>Future Projects</h3>
  <div class="project-photo" role="img" aria-label="Photo of a new residential street at sunset" style="background:linear-gradient(180deg,#a9c6e2,#e2c9a8 50%,#9a8f7c)"></div>
  <ul><li>Fusce id magna metus, ut interdum</li><li>Duis in eros in ipsum porttitor mattis</li><li>Etiam ac urna id velit eleifend ultric</li></ul>
</section>

<nav class="abs footer-links"><a href="#">Overview</a>|<a href="#">Current Projects</a>|<a href="#">Completed Projects</a>|<a href="#">Future Projects</a>|<a href="#">Sitemap</a>|<a href="#">Privacy Policy</a></nav>
<div class="abs footer-call">CALL <b>3812 4471</b></div>
<div class="abs copyright">Copyright © 2011 KT Developments P/L</div>
<div class="abs social"><span style="background:#3b5b98"></span><span style="background:#3fa9d8"></span><span style="background:#1f73a8"></span></div>
</body>
</html>
```